Dorian Felsgrove breaking. Or D. Felsgrove breaking

I break in and train horses, any age any bread of horse, for any disaplin. I need a business card that is simple but effective, in the way of looking professional. I would like a horse on my card, preferably a horse without a rider. I also pre train horse, younge horses that need a bit of riding before they go into serious work, and prepare yearlings for sale.

Reason: This is for my boyfriend, and I really want it to be perfect and impressive!

Target Market(s)

Thoroughbred race horse trainers, horse industrie people.

Industry/Entity Type

Business

Contact Information for Business Card

Dorian Felsgrove horse breaking, "WOLBUNDA" Armidale, give your horse the right start to any career. dfels@quillmail.com.au, 0431862097. Horse breaking~pre-training~sale preparation

```html
<!DOCTYPE html>
<html lang="en">
<head>
<meta charset="utf-8">
<title>Dorian Felsgrove Horse Breaking – Business Card</title>
<link rel="stylesheet" href="https://fonts.googleapis.com/css2?family=Jost:wght@300;400;600&family=Yellowtail&family=Kaushan+Script&display=block">
<style>
  :root {
    --page-bg: #e9e8e6;
    --card-white: #f4f4f3;
    --card-grey: #e6e7e7;
    --ink: #1d1d1d;
    --ink-soft: #3a3a3a;
    --photo-dark: #3c3d3e;
    --photo-mid: #8d8f90;
    --photo-light: #d7d8d8;
    --shadow: rgba(0, 0, 0, 0.18);
  }
  * { box-sizing: border-box; margin: 0; padding: 0; }
  html, body {
    width: 1200px;
    height: 880px;
    overflow: hidden;
    background: var(--page-bg);
  }
  .canvas {
    position: relative;
    width: 1200px;
    height: 880px;
  }
  .card {
    position: absolute;
    left: 250px;
    width: 700px;
    height: 400px;
    overflow: hidden;
    box-shadow: 0 6px 18px var(--shadow);
  }

  /* Front: name and contact */
  .card--front {
    top: 25px;
    background: linear-gradient(160deg, var(--card-white) 0%, var(--card-grey) 100%);
  }
  .front-photo {
    position: absolute;
    right: -40px;
    top: 60px;
    width: 420px;
    height: 360px;
    background: radial-gradient(ellipse at 60% 55%, rgba(140, 142, 143, 0.28) 0%, rgba(200, 201, 201, 0.15) 45%, rgba(230, 231, 231, 0) 75%);
  }
  .tagline {
    position: absolute;
    left: 30px;
    right: 30px;
    top: 36px;
    text-align: center;
    font-family: "Yellowtail", "Kaushan Script", cursive;
    font-size: 34px;
    line-height: 1.2;
    color: var(--ink);
    white-space: nowrap;
  }
  .identity {
    position: absolute;
    right: 48px;
    top: 150px;
    text-align: right;
  }
  .identity__name {
    font-family: "Jost", sans-serif;
    font-weight: 600;
    font-size: 31px;
    letter-spacing: 0.2em;
    color: var(--ink);
    text-transform: uppercase;
  }
  .identity__trade {
    font-family: "Jost", sans-serif;
    font-weight: 300;
    font-size: 23px;
    letter-spacing: 0.06em;
    color: var(--ink-soft);
    text-transform: uppercase;
    margin-top: 4px;
    margin-right: 40px;
  }
  .contact {
    position: absolute;
    left: 110px;
    bottom: 44px;
    display: flex;
    align-items: center;
    gap: 20px;
    font-family: "Jost", sans-serif;
    font-weight: 400;
    font-size: 23px;
    color: var(--ink);
    letter-spacing: 0.03em;
  }
  .contact__dot {
    width: 8px;
    height: 8px;
    border-radius: 50%;
    background: var(--ink);
  }

  /* Back: services */
  .card--back {
    top: 455px;
    background: var(--card-grey);
  }
  .back-photo {
    position: absolute;
    inset: 0;
    background:
      radial-gradient(ellipse 28% 42% at 70% 68%, rgba(60, 61, 62, 0.85) 0%, rgba(60, 61, 62, 0.45) 55%, rgba(60, 61, 62, 0) 100%),
      linear-gradient(100deg, var(--photo-light) 0%, var(--photo-light) 28%, #a9abac 55%, #bfc0c1 80%, #d0d1d1 100%);
  }
  .services {
    position: absolute;
    left: 48px;
    bottom: 46px;
    list-style: none;
    font-family: "Jost", sans-serif;
    font-weight: 400;
    font-size: 24px;
    letter-spacing: 0.05em;
    color: var(--ink);
    text-transform: uppercase;
  }
  .services li {
    display: flex;
    align-items: center;
    gap: 14px;
    line-height: 1.5;
  }
  .services li::before {
    content: "";
    width: 7px;
    height: 7px;
    border-radius: 50%;
    background: var(--ink);
  }
</style>
</head>
<body>
<main class="canvas">
  <section class="card card--front">
    <div class="front-photo" role="img" aria-label="Faint close-up photograph of a horse's eye"></div>
    <p class="tagline">Give your horse the right start to any career.</p>
    <div class="identity">
      <h1 class="identity__name">Dorian Felsgrove</h1>
      <p class="identity__trade">Horse Breaking</p>
    </div>
    <p class="contact">
      <span>dfels@quillmail.com.au</span>
      <span class="contact__dot"></span>
      <span>0431 862 097</span>
    </p>
  </section>

  <section class="card card--back">
    <div class="back-photo" role="img" aria-label="Black and white close-up photograph of a horse's eye and forelock"></div>
    <ul class="services">
      <li>Horse Breaking</li>
      <li>Pre-Training</li>
      <li>Sale Preparation</li>
    </ul>
  </section>
</main>
</body>
</html>
```